I need new business cards designed

I would like to get some new designs on business cards. I will upload my logo for reference. The business cards that were designed for me a few months ago were too difficult for the print companies to work with. My company is Brivoldex.com LLC. It is an art company that sells painting and expression cards online.

```html
<!DOCTYPE html>
<html lang="en">
<head>
<meta charset="utf-8">
<title>Brivoldex.com LLC — Business Card</title>
<link rel="stylesheet" href="https://fonts.googleapis.com/css2?family=Hind:wght@400;500;600&family=Montserrat:wght@700;800&display=swap">
<style>
  :root {
    --backdrop: #d3d3d5;
    --paper: #f4f4f3;
    --navy: #1d2270;
    --sky: #0fa7e0;
    --orange: #f29117;
    --clay: #dd7d40;
    --red: #ea1c22;
    --green: #7ac52d;
    --card-w: 760px;
    --card-h: 434px;
  }
  * { box-sizing: border-box; margin: 0; padding: 0; }
  html, body { width: 887px; height: 1200px; overflow: hidden; }
  body {
    background: var(--backdrop);
    font-family: "Hind", sans-serif;
    color: var(--navy);
    position: relative;
  }
  .card {
    position: absolute;
    left: 63px;
    width: var(--card-w);
    height: var(--card-h);
    background: var(--paper);
    overflow: hidden;
    box-shadow: 0 18px 40px rgba(0,0,0,0.18);
  }
  .card--front { top: 110px; }
  .card--back { top: 650px; }

  /* Front */
  .brand {
    position: absolute;
    left: 200px;
    top: 160px;
    display: flex;
    align-items: center;
    gap: 22px;
  }
  .brand__square {
    width: 86px;
    height: 86px;
    background: var(--orange);
    flex: none;
  }
  .brand__name {
    font-size: 50px;
    font-weight: 500;
    line-height: 1;
    color: var(--navy);
    letter-spacing: 0.5px;
  }
  .brand__tagline {
    font-size: 24px;
    font-weight: 400;
    line-height: 1;
    margin-top: 6px;
  }
  .tag--sky { color: var(--sky); }
  .tag--orange { color: var(--orange); }
  .tag--dot { color: var(--green); padding: 0 6px; }
  .front-rule {
    position: absolute;
    left: 0; bottom: 0;
    width: 100%;
    height: 14px;
    display: flex;
    flex-direction: column;
  }
  .front-rule__line { flex: 1; }
  .front-rule__line--navy { background: var(--navy); }
  .front-rule__line--sky { background: var(--sky); }

  /* Back */
  .back-band {
    position: absolute;
    left: 0; top: 0;
    width: 100%;
    height: 120px;
    display: flex;
    border-bottom: 6px solid var(--navy);
  }
  .back-band__block { flex: 1; }
  .back-band__block--sky { background: var(--sky); }
  .back-band__block--green { background: var(--green); }
  .back-band__block--orange { background: var(--orange); }
  .back-band__block--red { background: var(--red); }
  .holder {
    position: absolute;
    left: 44px;
    top: 196px;
  }
  .holder__name {
    font-family: "Montserrat", sans-serif;
    font-weight: 800;
    font-size: 40px;
    line-height: 1;
    letter-spacing: -0.5px;
  }
  .holder__role {
    font-family: "Montserrat", sans-serif;
    font-weight: 700;
    font-size: 12px;
    letter-spacing: 3.6px;
    margin-top: 6px;
  }
  .contact {
    list-style: none;
    margin-top: 16px;
    font-size: 15px;
    line-height: 1.3;
  }
  .contact__label { font-weight: 600; }
</style>
</head>
<body>

<section class="card card--front" aria-label="Card front">
  <div class="brand">
    <div class="brand__square"></div>
    <div>
      <div class="brand__name">Brivoldex.com</div>
      <div class="brand__tagline">
        <span class="tag--sky">Paint</span><span class="tag--dot">•</span><span class="tag--orange">Express</span><span class="tag--dot">•</span><span class="tag--orange">Share</span>
      </div>
    </div>
  </div>
  <div class="front-rule" aria-hidden="true">
    <div class="front-rule__line front-rule__line--sky"></div>
    <div class="front-rule__line front-rule__line--navy"></div>
  </div>
</section>

<section class="card card--back" aria-label="Card back">
  <div class="back-band" aria-hidden="true">
    <div class="back-band__block back-band__block--sky"></div>
    <div class="back-band__block back-band__block--green"></div>
    <div class="back-band__block back-band__block--orange"></div>
    <div class="back-band__block back-band__block--red"></div>
  </div>

  <div class="holder">
    <h1 class="holder__name">Jhone doe</h1>
    <p class="holder__role">COMPANY MANAGER</p>
    <ul class="contact">
      <li><span class="contact__label">Address</span> : 12 Fernway Rd,<br>Calder Bay 40218</li>
      <li><span class="contact__label">Web</span> : Brivoldex.com LLC</li>
      <li><span class="contact__label">Tele</span> : (555) 555-0198</li>
      <li><span class="contact__label">Mail</span> : hello@brivoldex.com</li>
    </ul>
  </div>
</section>

</body>
</html>
```